QORVIX needs a new business card!

QORVIX is a group of gaming enthusiasts who are looking for a new corporate business card.

The typeface should be modern and minimalist with attention paid to spacing between the letters and the letters 'qorvix' look relative to each other.

Should clean, crisp and minimalist - looking serious overall but with slight tweaks to the letters to make them look playful...

Black on white is fine.

Details on the card should include:
-the word 'qorvix'
-a job title (use any, for e.g. founder)
-a name (e.g. Ned Pallister)
-phone number
-email address

For inspiration: http://brevant.tamblework-cdn.example/wp-content/uploads/2013/07/kelo-1.jpg

Target Market(s)

Video gaming enthusiasts

Industry/Entity Type

Business

Requirements
Must have
• Black letter on white background.
The word "qorvix"
Nice to have
• Maybe use a conservative font like Gibraltar or Helvetica and tweaking each letter individually.

You can insert normal job titles under the "qorvix" typeface
Should not have
• Should not be cartoony or childish fonts. No colors.

```html
<!DOCTYPE html>
<html lang="en">
<head>
<meta charset="utf-8">
<title>QORVIX Business Card</title>
<link rel="stylesheet" href="https://fonts.googleapis.com/css2?family=Open+Sans:wght@600;700&display=swap">
<style>
  :root {
    --ink: #000000;
    --paper: #ffffff;
    --stage-light: #ffffff;
    --stage-light-glow: #e6e6e6;
    --stage-dark: #0d0d0f;
    --stage-dark-edge: #17171a;
  }
  html, body {
    margin: 0;
    padding: 0;
    width: 1200px;
    height: 1000px;
    overflow: hidden;
  }
  .presentation {
    position: relative;
    width: 1200px;
    height: 1000px;
    font-family: "Open Sans", Arial, sans-serif;
  }
  .stage {
    position: absolute;
    top: 0;
    height: 1000px;
  }
  .stage--light {
    left: 0;
    width: 604px;
    background: radial-gradient(ellipse 340px 420px at 290px 510px, var(--stage-light-glow) 0%, var(--stage-light) 100%);
  }
  .stage--dark {
    left: 604px;
    width: 596px;
    background: linear-gradient(90deg, var(--stage-dark) 0%, var(--stage-dark-edge) 50%, var(--stage-dark) 100%);
  }
  .card {
    position: absolute;
    width: 278px;
    height: 430px;
    overflow: hidden;
  }
  .card--dark {
    left: 142px;
    top: 295px;
    background: var(--ink);
    color: var(--paper);
    box-shadow: 0 14px 30px rgba(0, 0, 0, 0.35);
  }
  .card--light {
    left: 782px;
    top: 285px;
    background: var(--paper);
    color: var(--ink);
    box-shadow: 0 12px 26px rgba(0, 0, 0, 0.6);
  }
  .card__corner {
    position: absolute;
    top: 0;
    right: 0;
  }
  .card--dark .card__corner { top: 7px; right: 8px; }
  .card__wordmark {
    position: absolute;
    left: 33px;
    top: 36px;
    margin: 0;
    font-size: 72px;
    font-weight: 700;
    letter-spacing: -3px;
    line-height: 1;
    white-space: nowrap;
  }
  .card__details {
    position: absolute;
    left: 33px;
    top: 310px;
    margin: 0;
    padding: 0;
    list-style: none;
    font-size: 14px;
    font-weight: 600;
    line-height: 21px;
    letter-spacing: 0.2px;
  }
  .card__details li span {
    padding: 0 3px;
  }
  .card--dark .card__details li span {
    background: var(--paper);
    color: var(--ink);
  }
  .card--light .card__details li span {
    background: var(--ink);
    color: var(--paper);
  }
</style>
</head>
<body>
<main class="presentation">
  <section class="stage stage--light"></section>
  <section class="stage stage--dark"></section>

  <article class="card card--dark">
    <svg class="card__corner" width="56" height="56" viewBox="0 0 56 56" aria-hidden="true">
      <polygon points="0,0 56,0 56,56" fill="var(--paper)"/>
    </svg>
    <h1 class="card__wordmark">qorvix</h1>
    <ul class="card__details">
      <li><span>Founder</span></li>
      <li><span>Ned Pallister</span></li>
      <li><span>+44 000 000</span></li>
      <li><span>nedpallister@qorvix.com</span></li>
    </ul>
  </article>

  <article class="card card--light">
    <svg class="card__corner" width="56" height="56" viewBox="0 0 56 56" aria-hidden="true">
      <polygon points="0,0 56,0 56,56" fill="var(--ink)"/>
    </svg>
    <h1 class="card__wordmark">qorvix</h1>
    <ul class="card__details">
      <li><span>Founder</span></li>
      <li><span>Ned Pallister</span></li>
      <li><span>+44 000 000</span></li>
      <li><span>nedpallister@qorvix.com</span></li>
    </ul>
  </article>
</main>
</body>
</html>
```